Postcard Design

A house cleaning business. Focus on time saving and stress free. Free estimates. Want it to state that we can make your home sparkle or shine. I have been using the colors purple and black in the logo which I will attach.

Reason: I need a few more days to decide on this. Thank you

Industry/Entity Type

House

Colors
886aae
6b449b

Requirements
Must have
• website www.tidwellhavenhomes.us
phone # 555-390-6172

```html
<!DOCTYPE html>
<html lang="en">
<head>
<meta charset="utf-8">
<title>Tidwell Haven Homes – Postcard</title>
<link href="https://fonts.googleapis.com/css2?family=Open+Sans:wght@400;600;700&display=swap" rel="stylesheet">
<style>
  :root {
    --purple: #6b449b;
    --purple-soft: #886aae;
    --purple-pale: #d9cde8;
    --ink: #1c1c1c;
    --grey-band: #c9c9cc;
    --charcoal: #3a3a3d;
    --paper: #ffffff;
    --stage: #eeeae4;
  }
  * { box-sizing: border-box; margin: 0; padding: 0; }
  html, body { width: 1200px; height: 680px; overflow: hidden; }
  body {
    background: var(--stage);
    font-family: "Open Sans", Arial, sans-serif;
    color: var(--ink);
    position: relative;
  }

  /* ---------- Front of postcard ---------- */
  .postcard-front {
    position: absolute; left: 50px; top: 33px;
    width: 472px; height: 605px;
    background: var(--paper);
    overflow: hidden;
  }
  .front-header {
    height: 60px; background: var(--purple);
    color: #fff; font-size: 25px; font-weight: 400;
    display: flex; align-items: center; justify-content: center;
  }
  .room-photo {
    position: absolute; left: 0; top: 60px; width: 472px; height: 320px;
    background: linear-gradient(160deg, #f3efe9 0%, #e6ddd0 45%, #d8cfc4 70%, #efe9e2 100%);
  }
  .front-swoosh { position: absolute; left: 0; top: 220px; width: 472px; height: 240px; }
  .front-brand {
    position: absolute; right: 30px; top: 400px;
    display: flex; align-items: center; gap: 12px;
  }
  .brand-dot { width: 22px; height: 22px; border-radius: 50%; background: var(--purple); }
  .brand-name { font-size: 28px; font-weight: 700; color: var(--purple); line-height: 1.1; }
  .front-tagline {
    position: absolute; left: 22px; top: 448px;
    font-size: 19px; color: var(--purple-soft); line-height: 1.3;
  }
  .front-footer {
    position: absolute; left: 0; bottom: 0; width: 100%; height: 88px;
    background: var(--grey-band);
    display: flex; justify-content: space-between; align-items: center;
    padding: 0 14px 0 20px;
  }
  .service-blurb { width: 210px; font-size: 10.5px; line-height: 1.35; color: var(--ink); }
  .estimate { text-align: left; }
  .estimate-lead { font-size: 14px; font-weight: 600; color: var(--purple); }
  .estimate-phone {
    display: flex; align-items: center; gap: 8px;
    font-size: 25px; font-weight: 600; color: var(--charcoal); margin-top: 4px;
  }
  .estimate-phone svg { width: 26px; height: 26px; }

  /* ---------- Back of postcard ---------- */
  .postcard-back {
    position: absolute; left: 558px; top: 170px;
    width: 605px; height: 445px;
    background: var(--paper);
  }
  .back-panel {
    position: absolute; left: 0; top: 0; width: 338px; height: 397px;
    background: var(--paper);
    border: 1px solid #bdbdbd; border-top: none; border-left: none;
    border-bottom-right-radius: 14px;
  }
  .back-header {
    height: 56px; background: var(--purple); color: #fff;
    font-size: 17px; display: flex; align-items: center; padding-left: 42px;
  }
  .contact { padding: 28px 0 0 22px; font-size: 12px; line-height: 1.5; }
  .contact-title {
    display: inline-block; font-size: 13px; font-weight: 600;
    border-bottom: 1px solid var(--purple-soft); padding-right: 128px; margin-bottom: 10px;
  }
  .contact-company { margin-bottom: 10px; }
  .contact strong { font-weight: 600; }
  .back-brand {
    position: absolute; left: 70px; top: 270px;
    display: flex; align-items: center; gap: 10px;
  }
  .back-brand .brand-name { font-size: 22px; }
  .back-brand .brand-dot { width: 18px; height: 18px; }
  .web-pill {
    position: absolute; left: 9px; top: 395px; width: 288px; height: 33px;
    background: var(--purple-soft); color: #fff; border-radius: 17px;
    font-size: 14px; font-weight: 600;
    display: flex; align-items: center; padding-left: 40px;
  }
  .stamp-box {
    position: absolute; left: 488px; top: 18px; width: 92px; height: 75px;
    border: 1px solid #9a9a9a;
  }
  .address-line {
    position: absolute; left: 350px; width: 228px; height: 1px; background: #9a9a9a;
  }
  .back-strip {
    position: absolute; left: 0; bottom: 0; width: 100%; height: 8px; background: var(--charcoal);
  }
</style>
</head>
<body>

<section class="postcard-front">
  <header class="front-header">We can make your house sparkle!</header>
  <div class="room-photo" role="img" aria-label="Bright, tidy living room with white sofas, lamps and a chandelier"></div>
  <svg class="front-swoosh" viewBox="0 0 472 240" aria-hidden="true">
    <path d="M0 70 C120 150 300 120 472 30 L472 240 L0 240 Z" fill="var(--purple-soft)" opacity="0.75"/>
    <path d="M0 120 C140 190 320 150 472 70 L472 240 L0 240 Z" fill="var(--purple)" opacity="0.85"/>
    <path d="M0 160 C150 230 330 200 472 120 L472 240 L0 240 Z" fill="#ffffff"/>
  </svg>
  <div class="front-brand">
    <span class="brand-dot"></span>
    <span class="brand-name">Tidwell Haven Homes</span>
  </div>
  <p class="front-tagline">A sparking shine,<br>Every time!</p>
  <footer class="front-footer">
    <p class="service-blurb">Tidwell Haven Homes offers old fashion, high-quality home cleaning services. Our professionals are insured and bonded.</p>
    <div class="estimate">
      <p class="estimate-lead">Call today for a Free Estimate!</p>
      <p class="estimate-phone">
        <svg viewBox="0 0 26 26" aria-hidden="true"><path d="M4 24 V12 Q4 6 10 6 H16 V1 L25 9.5 L16 18 V13 H11 Q10 13 10 14 V24 Z" fill="var(--purple)"/></svg>
        555-390-6172
      </p>
    </div>
  </footer>
</section>

<section class="postcard-back">
  <div class="back-panel">
    <header class="back-header">A sparking shine, Every time!</header>
    <div class="contact">
      <p class="contact-title">Contact Us:</p>
      <p class="contact-company">Tidwell Haven Homes</p>
      <p>Phone: <strong>555-390-6172</strong></p>
      <p>Email: <strong>hello@tidwellhavenhomes.us</strong></p>
    </div>
    <div class="back-brand">
      <span class="brand-dot"></span>
      <span class="brand-name">Tidwell Haven Homes</span>
    </div>
  </div>
  <div class="web-pill">www.tidwellhavenhomes.us</div>
  <div class="stamp-box"></div>
  <div class="address-line" style="top:217px"></div>
  <div class="address-line" style="top:262px"></div>
  <div class="address-line" style="top:307px"></div>
  <div class="back-strip"></div>
</section>

</body>
</html>
```